Chia Seed Standup Pouch package design

We are looking for a clean and beautiful standup packaging design for our Organic Chia Seeds.

The package should have a healthy, natural, clean feel to it.

Please see attached Chia Seeds Packaging Samples for further instructions.

***** Requirements *****
- We want two bag style but one design. One will be with a spout and one without a spout.

- Print ready with bleed lines

Reason: We are extending the contest to allow for designers to perfect their designs. Some designs are coming real close to what we would be happy with. Price is now guaranteed. Thank you all for your designs.

Target Market(s)

Health and weight conscious individuals. Our target market are looking for whole natural foods.

Requirements
Must have
• - Include NFCB Organic logo (at minimum, can also include gluten free, vegan, etc)

On the back side of the package:
- have a place that promote our Chia Tea products. For example: "Also try our Natural Instant Chia Tea, made with Premium organic chia seeds and natural fruits and herbs extracts. (Chia Tea images attached)
Nice to have
• product highlights such as fiber, omega 3, protein, antioxidants, etc.

```html
<!DOCTYPE html>
<html lang="en">
<head>
<meta charset="utf-8">
<title>Sunleaf Nutrition – Organic Raw Chia Seeds Pouch</title>
<link rel="stylesheet" href="https://fonts.googleapis.com/css2?family=Signika:wght@400;600;700&display=swap">
<style>
  :root {
    --bg: #ffffff;
    --pouch-white: #fbfbf9;
    --pouch-edge: #e6e7e3;
    --green: #8cc63f;
    --green-light: #a6d55a;
    --green-dark: #6fae2c;
    --yellow: #f6c90e;
    --yellow-light: #fde15a;
    --ink-dark: #5a4a10;
    --white: #ffffff;
    --seed-dark: #3b3d3a;
    --seed-light: #a9aaa4;
  }
  * { margin: 0; padding: 0; box-sizing: border-box; }
  html, body {
    width: 1200px; height: 675px; overflow: hidden;
    background: var(--bg);
    font-family: "Signika", "Trebuchet MS", sans-serif;
  }
  .canvas { position: relative; width: 1200px; height: 675px; }

  .pouch {
    position: absolute; left: 420px; top: 40px;
    width: 360px; height: 590px;
    background: var(--pouch-edge);
    border-radius: 6px;
    padding: 12px 12px 0;
    overflow: hidden;
  }
  .pouch-face {
    position: relative; width: 100%; height: 100%;
    background: var(--pouch-white);
    overflow: hidden;
  }
  .pouch-band {
    position: absolute; left: 0; top: 110px; width: 100%; height: calc(100% - 110px);
  }
  .pouch-band svg { display: block; width: 100%; height: 100%; }

  .brand {
    position: absolute; top: 34px; left: 0; width: 100%;
    display: flex; align-items: center; justify-content: center; gap: 10px;
  }
  .brand-dot {
    width: 34px; height: 34px; border-radius: 50%;
    border: 3px solid var(--yellow);
  }
  .brand-name {
    color: var(--yellow); font-weight: 600; font-size: 21px; line-height: 1;
    letter-spacing: 0.5px; text-transform: uppercase;
  }

  .label {
    position: absolute; top: 140px; left: 0; width: 100%;
    text-align: center; color: var(--white);
  }
  .label-kicker { font-weight: 600; font-size: 19px; }
  .label-title { font-weight: 600; font-size: 50px; line-height: 1.05; letter-spacing: 0.5px; }
  .label-pill {
    display: inline-block; margin-top: 6px;
    background: linear-gradient(var(--yellow-light), var(--yellow));
    color: var(--ink-dark); font-weight: 600; font-size: 17px;
    padding: 3px 18px; border-radius: 8px;
  }
  .label-facts { margin-top: 8px; font-weight: 600; font-size: 14.5px; }

  .seed-window {
    position: absolute; top: 350px; left: 50%; transform: translateX(-50%);
    width: 140px; height: 140px; border-radius: 50%;
    border: 6px solid var(--yellow);
    background: radial-gradient(circle, var(--seed-light) 0%, var(--seed-dark) 70%, var(--seed-light) 100%);
  }

  .badges {
    position: absolute; bottom: 20px; left: 0; width: 100%;
    display: flex; justify-content: center; gap: 10px;
  }
  .badge { width: 44px; text-align: center; color: var(--white); }
  .badge-mark {
    width: 22px; height: 22px; margin: 0 auto 3px;
    border-radius: 50%; border: 2px solid var(--white);
  }
  .badge-text { font-size: 6px; font-weight: 600; text-transform: uppercase; line-height: 1.1; }
</style>
</head>
<body>
<main class="canvas">
  <section class="pouch" aria-label="Chia seeds standup pouch, front">
    <div class="pouch-face">
      <div class="pouch-band">
        <svg viewBox="0 0 336 468" preserveAspectRatio="none" aria-hidden="true">
          <defs>
            <linearGradient id="bandFill" x1="0" y1="0" x2="0" y2="1">
              <stop offset="0" stop-color="#9ccf4d"/>
              <stop offset="1" stop-color="#86c23a"/>
            </linearGradient>
          </defs>
          <path d="M0 8 Q168 -4 336 8 L336 468 L0 468 Z" fill="url(#bandFill)"/>
          <path d="M0 2 Q168 -10 336 2" fill="none" stroke="#8cc63f" stroke-width="1.5"/>
        </svg>
      </div>

      <div class="brand">
        <span class="brand-dot"></span>
        <span class="brand-name">Sunleaf Nutrition</span>
      </div>

      <div class="label">
        <p class="label-kicker">100% Organic Raw</p>
        <h1 class="label-title">Chia Seeds</h1>
        <p class="label-pill">Ancient Aztec Superfood</p>
        <p class="label-facts">2.5 g Omega, 30 g Protein, 5 g Fiber</p>
      </div>

      <div class="seed-window" role="img" aria-label="Window showing raw black and white chia seeds"></div>

      <ul class="badges" style="list-style:none">
        <li class="badge"><div class="badge-mark"></div><div class="badge-text">NFCB Certified</div></li>
        <li class="badge"><div class="badge-mark"></div><div class="badge-text">Vegetarian</div></li>
        <li class="badge"><div class="badge-mark"></div><div class="badge-text">GMO Free</div></li>
        <li class="badge"><div class="badge-mark"></div><div class="badge-text">Gluten Free</div></li>
        <li class="badge"><div class="badge-mark"></div><div class="badge-text">Vegan</div></li>
        <li class="badge"><div class="badge-mark"></div><div class="badge-text">Nothing Artificial</div></li>
      </ul>
    </div>
  </section>
</main>
</body>
</html>
```